"Tidelark Ministry" needs a logo design that represents a Christian family boating ministry

Mission Statement:
“Providing compassion, care and opportunities to create memories for marginalized groups of society through ocean therapy.”
Bible verse:
Colossians 3:12 – “Therefore, as God’s chosen people, holy and dearly loved, clothe yourselves with compassion, kindness, humility, gentleness and patience.”
Target Market(s)
HOMELESS (who have gone through shelters and are on the road to recovery)
CHURCH GROUPS
INJURED MILITARY VETERANS
YOUTH AT RISK (orphans, human trafficking survivors)
SICKLY (hospitalized who can get out once in a while)
CAREGIVERS (single moms, military spouses caring for injured vets, families of those in prison)
ELDERLY (retirement centers)
SMALL BUSINESS STAFF OUTINGS
SPECIAL EVENTS
Industry/Entity Type
Ministry
Contact Information for Business Card
Captain Glen Marbury @ 555-014-2931
Priscilla Marbury @ 555-018-6457
info@tidelarkministry-example.com
www.tidelarkministry-example.com (not active yet but hopefully, soon)
Requirements
Must have
- Catch-phrase words maybe for back of business card:
- "Tidelark --- Kindness --- Sharing days on the waves"
Nice to have
- Added 2 photo files just for visuals:
- 1 photo is of our boat.
- Other photo is our daughter's artwork on a cooler she made (for father's day gift)...might be nice and fun to incorporate daughter's artwork/inspiration into logo...but not sure if it looks to busy

```html
<!DOCTYPE html>
<html lang="en">
<head>
<meta charset="utf-8">
<title>Tidelark Ministry – Business Card</title>
<link href="https://fonts.googleapis.com/css2?family=Open+Sans:wght@400;700&display=swap" rel="stylesheet">
<style>
  :root {
    --page-bg: #e9e6e2;
    --ocean-deep: #0b4a73;
    --ocean-mid: #13729c;
    --ocean-light: #2a8fb4;
    --sail-violet: #3f4a93;
    --sail-haze: #6b76b3;
    --sea-navy: #2c3477;
    --ink-white: #ffffff;
    --card-shadow: rgba(0, 0, 0, 0.28);
  }
  * { box-sizing: border-box; margin: 0; padding: 0; }
  html, body {
    width: 1200px; height: 850px; overflow: hidden;
    background: var(--page-bg);
    font-family: "Open Sans", Arial, sans-serif;
    color: var(--ink-white);
  }
  .stage { position: relative; width: 1200px; height: 850px; }

  .card {
    position: absolute;
    width: 540px; height: 310px;
    border-radius: 4px;
    overflow: hidden;
    box-shadow: 0 10px 28px var(--card-shadow);
  }
  .card-photo { position: absolute; inset: 0; }

  /* Front */
  .card-front { left: 70px; top: 110px; }
  .card-front .card-photo {
    background: radial-gradient(ellipse at 60% 10%, var(--ocean-light) 0%, var(--ocean-mid) 40%, var(--ocean-deep) 100%);
  }
  .contact {
    position: absolute;
    padding-left: 12px;
    border-left: 1.5px solid var(--ink-white);
  }
  .contact-captain { left: 36px; top: 118px; }
  .contact-partner { left: 340px; top: 88px; }
  .contact-name { font-weight: 700; font-size: 17px; line-height: 1; }
  .contact-phone { font-weight: 400; font-size: 17px; margin-top: 22px; line-height: 1; }
  .role-icon { position: absolute; }
  .icon-wheel { left: 102px; top: 44px; }
  .icon-anchor { left: 418px; top: 20px; }

  .web-lines { position: absolute; left: 108px; top: 214px; }
  .web-line { display: flex; align-items: center; gap: 14px; height: 34px; }
  .web-line span { font-weight: 700; font-size: 16px; }

  /* Back */
  .card-back { left: 600px; top: 450px; }
  .card-back .card-photo {
    background: linear-gradient(165deg, var(--sail-haze) 0%, var(--sail-violet) 45%, var(--sea-navy) 100%);
  }
  .slogan {
    position: absolute; left: 110px; top: 44px;
    padding-left: 22px;
    border-left: 2px solid var(--ink-white);
  }
  .slogan p { font-weight: 700; font-size: 31px; line-height: 1.1; margin-bottom: 26px; }
  .slogan p:last-child { margin-bottom: 0; }
</style>
</head>
<body>
<main class="stage">

  <section class="card card-front" aria-label="Tidelark Ministry business card, front">
    <div class="card-photo" role="img" aria-label="Underwater ocean photograph in deep blue tones"></div>

    <svg class="role-icon icon-wheel" width="56" height="56" viewBox="0 0 56 56" fill="none" stroke="#fff" stroke-width="2.4" aria-hidden="true">
      <circle cx="28" cy="28" r="15"/>
      <circle cx="28" cy="28" r="6"/>
      <path d="M28 4v18M28 34v18M4 28h18M34 28h18M11 11l13 13M32 32l13 13M45 11L32 24M24 32L11 45"/>
    </svg>

    <svg class="role-icon icon-anchor" width="50" height="60" viewBox="0 0 50 60" fill="none" stroke="#fff" stroke-width="3.2" stroke-linecap="round" aria-hidden="true">
      <circle cx="25" cy="8" r="5"/>
      <path d="M25 13v42M15 22h20M5 36c2 12 12 19 20 19s18-7 20-19M5 36l-3 5M5 36l6 2M45 36l3 5M45 36l-6 2"/>
    </svg>

    <div class="contact contact-captain">
      <p class="contact-name">Captain Glen Marbury</p>
      <p class="contact-phone">555-014-2931</p>
    </div>
    <div class="contact contact-partner">
      <p class="contact-name">Priscilla Marbury</p>
      <p class="contact-phone">555-018-6457</p>
    </div>

    <div class="web-lines">
      <div class="web-line">
        <svg width="36" height="20" viewBox="0 0 36 20" fill="none" stroke="#fff" stroke-width="1.6" aria-hidden="true">
          <rect x="2" y="3" width="24" height="14" rx="5"/>
          <path d="M26 7h5v6h-5M31 8h3v4h-3"/>
        </svg>
        <span>info@tidelarkministry-example.com</span>
      </div>
      <div class="web-line">
        <svg width="36" height="24" viewBox="0 0 36 24" fill="none" stroke="#fff" stroke-width="1.6" aria-hidden="true">
          <path d="M18 2v16M18 3l-9 13h9M18 5l7 11h-7M6 19h24l-3 4H9z"/>
        </svg>
        <span>www.tidelarkministry-example.com</span>
      </div>
    </div>
  </section>

  <section class="card card-back" aria-label="Tidelark Ministry business card, back">
    <div class="card-photo" role="img" aria-label="Sailboat deck and sails on open sea under a violet tint"></div>
    <div class="slogan">
      <p>Tidelark</p>
      <p>Kindness</p>
      <p>Sharing days<br>on the waves</p>
    </div>
  </section>

</main>
</body>
</html>
```